Bramwell Business Cards

Logo files are included. Full "Bramwell" logo should be included on the back of the business card. The B symbol should be included on the front with the contact information.

Bramwell, LLC is the company name and we do commercial construction and real estate development consulting services. Look for a fairly simple card design utilizing our logo.

```html
<!DOCTYPE html>
<html lang="en">
<head>
<meta charset="utf-8">
<title>Bramwell Business Cards</title>
<link href="https://fonts.googleapis.com/css2?family=Mulish:wght@400;500;700;800&display=swap" rel="stylesheet">
<style>
  :root {
    --navy: #1b3a52;
    --gold: #e9ad1f;
    --paper: #ffffff;
    --backdrop: #efefef;
    --shadow: rgba(0, 0, 0, 0.16);
  }
  * { box-sizing: border-box; margin: 0; padding: 0; }
  html, body {
    width: 1187px;
    height: 1200px;
    overflow: hidden;
    background: var(--backdrop);
    font-family: "Mulish", Arial, sans-serif;
    color: var(--navy);
  }
  .sheet {
    width: 1187px;
    height: 1200px;
    display: flex;
    flex-direction: column;
    align-items: center;
    justify-content: center;
    gap: 40px;
  }
  .card {
    position: relative;
    width: 960px;
    height: 548px;
    background: var(--paper);
    box-shadow: 0 4px 18px var(--shadow);
    overflow: hidden;
  }
  .card-shape {
    position: absolute;
    inset: 0;
    width: 100%;
    height: 100%;
  }

  /* Brand side */
  .brand-mark {
    position: absolute;
    left: 480px;
    top: 160px;
    width: 150px;
    height: 150px;
    margin: -75px 0 0 -75px;
    border: 10px solid var(--navy);
    border-radius: 50%;
  }
  .brand-name {
    position: absolute;
    left: 0;
    right: 0;
    top: 270px;
    text-align: center;
    font-size: 88px;
    font-weight: 700;
    letter-spacing: 3px;
    line-height: 1;
    text-transform: uppercase;
    color: var(--navy);
  }
  .brand-rule {
    position: absolute;
    left: 210px;
    width: 540px;
    top: 380px;
    height: 2px;
    background: var(--navy);
  }
  .brand-tagline {
    position: absolute;
    left: 0;
    right: 0;
    top: 412px;
    text-align: center;
    font-size: 27px;
    font-weight: 600;
    line-height: 1.25;
    color: var(--navy);
  }

  /* Contact side */
  .person {
    position: absolute;
    left: 55px;
    top: 56px;
  }
  .person-name {
    font-size: 45px;
    line-height: 1;
    font-weight: 500;
  }
  .person-name strong { font-weight: 800; }
  .person-role {
    margin-top: 6px;
    font-size: 25px;
    font-weight: 500;
  }
  .phones {
    position: absolute;
    right: 52px;
    top: 62px;
    list-style: none;
    font-size: 24px;
    font-weight: 500;
    line-height: 38px;
  }
  .phones li {
    display: flex;
    align-items: center;
    gap: 10px;
  }
  .phones svg { width: 18px; height: 18px; }
  .contact-mark {
    position: absolute;
    left: 480px;
    top: 235px;
    transform: translate(-50%, -50%);
    font-size: 50px;
    font-weight: 700;
    line-height: 1;
    color: var(--navy);
  }
  .contact-lines {
    position: absolute;
    left: 0;
    right: 0;
    top: 440px;
    text-align: center;
    color: var(--paper);
    font-size: 24px;
    font-weight: 500;
    line-height: 39px;
  }
  .contact-lines .divider { color: var(--gold); padding: 0 3px; }
</style>
</head>
<body>
<main class="sheet">

  <section class="card card-brand" aria-label="Card brand side">
    <svg class="card-shape" viewBox="0 0 960 548" aria-hidden="true">
      <path d="M0 0 H960 Q480 280 0 0 Z" fill="var(--navy)"/>
      <circle cx="480" cy="160" r="106" fill="var(--paper)"/>
    </svg>
    <div class="brand-mark" aria-hidden="true"></div>
    <h1 class="brand-name">Bramwell</h1>
    <div class="brand-rule"></div>
    <p class="brand-tagline">Commercial Construction and Real Estate Development<br>Consulting Services</p>
  </section>

  <section class="card card-contact" aria-label="Card contact side">
    <svg class="card-shape" viewBox="0 0 960 548" aria-hidden="true">
      <path d="M0 548 Q480 -22 960 548 Z" fill="var(--navy)"/>
      <circle cx="480" cy="235" r="167" fill="var(--paper)"/>
    </svg>
    <div class="person">
      <h2 class="person-name"><strong>Daniel</strong> Hart</h2>
      <p class="person-role">Director</p>
    </div>
    <ul class="phones">
      <li>
        <svg viewBox="0 0 18 18" aria-hidden="true"><rect x="4" y="1" width="10" height="16" rx="2" fill="none" stroke="var(--gold)" stroke-width="2"/><circle cx="9" cy="13.5" r="1.2" fill="var(--gold)"/></svg>
        +000 2468 1357
      </li>
      <li>
        <svg viewBox="0 0 18 18" aria-hidden="true"><path d="M4 1.5 L7 5 L5.3 7 Q7.5 11 11 12.7 L13 11 L16.5 14 L14.5 16.5 Q8 16 4 11.5 Q1 7 1.5 3.5 Z" fill="var(--gold)"/></svg>
        +000 2468 1357
      </li>
    </ul>
    <p class="contact-mark">Bramwell</p>
    <p class="contact-lines">
      mail@bramwellllc.com <span class="divider">|</span> www.bramwellllc.com<br>
      18 Alder Ridge Road, Helena, MT 59601
    </p>
  </section>

</main>
</body>
</html>
```